Solar WiFi Charging Bench

Sales Brochure using only the colors of the Marigold Color Palette provided.
Municipal Government target customer.
Key Features are as follows:
LED Advertising display
Connection to internet (User Defined)
800W Solar
USB-A and USB-C cell phone charging ports
400ah battery backup with low voltage shutoff
Insulated for -40 Deg C
Wireless cell phone charging
Vandalism resistant.
Theft resistant

```html
<!DOCTYPE html>
<html lang="en">
<head>
<meta charset="utf-8">
<title>Marigold Renewables – Solar WiFi Charging Bench</title>
<link href="https://fonts.googleapis.com/css2?family=Poppins:wght@300;400;800;900&display=swap" rel="stylesheet">
<style>
  :root {
    --navy: #3d55a5;
    --sky: #4fc3ec;
    --white: #ffffff;
    --backdrop: #dcdcdc;
    --photo-sky: #c9d3da;
    --photo-grass: #8f8a5e;
    --photo-tree: #5e7a4c;
  }
  * { box-sizing: border-box; margin: 0; padding: 0; }
  html, body {
    width: 1152px; height: 1200px; overflow: hidden;
    background: var(--backdrop);
    font-family: "Poppins", sans-serif;
  }
  .brochure {
    position: absolute; left: 173px; top: 30px;
    width: 1192px; height: 1685px;
    transform: scale(0.6766); transform-origin: 0 0;
    background: var(--white);
    overflow: hidden;
  }
  .brand {
    position: absolute; left: 70px; top: 200px; width: 320px;
    display: flex; align-items: center; gap: 14px;
    color: var(--navy); font-weight: 800; font-size: 30px; line-height: 1.1;
    letter-spacing: 1px;
  }
  .brand-dot { width: 46px; height: 46px; border-radius: 50%; background: var(--sky); flex: none; }
  .headline { position: absolute; left: 68px; color: var(--navy); white-space: nowrap; z-index: 2; }
  .headline-strong { font-weight: 900; font-size: 52px; line-height: 1; }
  .headline-light { font-weight: 400; font-size: 54px; line-height: 1; }
  .headline-light.sky { color: var(--sky); font-weight: 300; }
  .title-solar { top: 400px; }
  .title-bench { top: 462px; }
  .title-led { top: 594px; }
  .title-display { top: 654px; }
  .rule { position: absolute; left: 68px; top: 558px; width: 242px; height: 3px; background: var(--sky); }
  .photo { position: absolute; }
  .photo-hero {
    left: 478px; top: 63px; width: 714px; height: 688px;
    border-bottom-left-radius: 160px 688px;
    background: linear-gradient(180deg, var(--photo-sky) 0%, #b9c2c4 45%, var(--photo-tree) 62%, var(--photo-grass) 100%);
  }
  .photo-front {
    left: 0; top: 768px; width: 692px; height: 409px;
    border-top-right-radius: 90px; border-bottom-right-radius: 110px;
    background: linear-gradient(180deg, #c6cfd4 0%, #7f9a6a 45%, var(--photo-grass) 80%, #5a4a3a 100%);
  }
  .photo-side {
    left: 708px; top: 772px; width: 455px; height: 682px;
    border-radius: 40px;
    background: linear-gradient(180deg, #cfd6da 0%, #6e8c58 35%, #a9a9a3 55%, var(--photo-grass) 85%, #5a4a3a 100%);
  }
  .feature-panel {
    position: absolute; left: 36px; top: 1177px; width: 656px; height: 508px;
    background: var(--navy); color: var(--white);
  }
  .feature-list { list-style: none; position: absolute; left: 32px; top: 24px; }
  .feature-list li {
    display: flex; align-items: center; gap: 9px;
    font-size: 24px; font-weight: 400; height: 42px; white-space: nowrap;
  }
  .tick { width: 16px; height: 16px; flex: none; }
  .contact { position: absolute; left: 32px; top: 372px; font-weight: 800; }
  .contact-phone { font-size: 32px; line-height: 1.2; }
  .contact-web { font-size: 26px; line-height: 1.1; }
</style>
</head>
<body>
<main class="brochure">
  <div class="brand"><span class="brand-dot"></span><span>MARIGOLD<br>RENEWABLES</span></div>

  <div class="photo photo-hero" role="img" aria-label="Solar charging bench with curved canopy installed on grass beside a library building"></div>

  <h1 class="headline headline-strong title-solar">Solar WiFi</h1>
  <p class="headline headline-light title-bench">Charging Bench</p>
  <div class="rule"></div>
  <h2 class="headline headline-strong title-led">LED Advertising</h2>
  <p class="headline headline-light sky title-display">display</p>

  <div class="photo photo-front" role="img" aria-label="Front view of the charging bench with wooden seat and LED display panel, trees behind"></div>
  <div class="photo photo-side" role="img" aria-label="Side view of the bench showing the solar panel canopy near a parking lot"></div>

  <section class="feature-panel">
    <ul class="feature-list">
      <li><svg class="tick" viewBox="0 0 16 16"><circle cx="8" cy="8" r="8" fill="#4fc3ec"/><path d="M4.5 8.2l2.3 2.3 4.7-4.8" stroke="#3d55a5" stroke-width="2" fill="none"/></svg>Connection to internet (User Defined)</li>
      <li><svg class="tick" viewBox="0 0 16 16"><circle cx="8" cy="8" r="8" fill="#4fc3ec"/><path d="M4.5 8.2l2.3 2.3 4.7-4.8" stroke="#3d55a5" stroke-width="2" fill="none"/></svg>800W Solar</li>
      <li><svg class="tick" viewBox="0 0 16 16"><circle cx="8" cy="8" r="8" fill="#4fc3ec"/><path d="M4.5 8.2l2.3 2.3 4.7-4.8" stroke="#3d55a5" stroke-width="2" fill="none"/></svg>USB-A and USB-C cell phone charging ports</li>
      <li><svg class="tick" viewBox="0 0 16 16"><circle cx="8" cy="8" r="8" fill="#4fc3ec"/><path d="M4.5 8.2l2.3 2.3 4.7-4.8" stroke="#3d55a5" stroke-width="2" fill="none"/></svg>400ah battery backup with low voltage shutoff</li>
      <li><svg class="tick" viewBox="0 0 16 16"><circle cx="8" cy="8" r="8" fill="#4fc3ec"/><path d="M4.5 8.2l2.3 2.3 4.7-4.8" stroke="#3d55a5" stroke-width="2" fill="none"/></svg>Insulated for -40 Deg C</li>
      <li><svg class="tick" viewBox="0 0 16 16"><circle cx="8" cy="8" r="8" fill="#4fc3ec"/><path d="M4.5 8.2l2.3 2.3 4.7-4.8" stroke="#3d55a5" stroke-width="2" fill="none"/></svg>Wireless cell phone charging</li>
      <li><svg class="tick" viewBox="0 0 16 16"><circle cx="8" cy="8" r="8" fill="#4fc3ec"/><path d="M4.5 8.2l2.3 2.3 4.7-4.8" stroke="#3d55a5" stroke-width="2" fill="none"/></svg>Vandalism resistant</li>
      <li><svg class="tick" viewBox="0 0 16 16"><circle cx="8" cy="8" r="8" fill="#4fc3ec"/><path d="M4.5 8.2l2.3 2.3 4.7-4.8" stroke="#3d55a5" stroke-width="2" fill="none"/></svg>Theft resistant</li>
    </ul>
    <div class="contact">
      <p class="contact-phone">Call +000 000 000</p>
      <p class="contact-web">www.web.com</p>
    </div>
  </section>
</main>
</body>
</html>
```